こんにちは、

森川建設の森川です!

弊社は、
八王子市で足場屋を営んでおります!

筋トレ大好きな若者向けの求人用のチラシを作ってもらいたいです。

アルバイト募集って感じで、

・ロングタイム
8:00〜17:00で1日16,000円

・ショートタイム
10:00〜16:00で1日13,000円

置き場などでの残業はありません。

筋肉、体幹を、鍛えて、
かつ、

ワンチャン技術も身につく!

※筋トレ好きや、格闘家や、アスリートに最適!

-----------------------------
弊社の売り(ここは、入れないほうが良ければ入れなくてもいいです!参考までに)

・会社の理念が、社員満足度を第一にして、会社と、関わる全ての人を潤わす。
・質の高い足場屋さん。技術力も優れている。
・週休2日制
・自分の用事に合わせて好きな日に休める。
・関わる全ての人が 経済的、精神的、時間的に潤うことを目指している。
・チームワークを大事にしている。
・全スタッフ14名
・イベント多数 (毎年海外旅行or国内旅行+レジャー)
・ホームページ morikawakensetsu.info

こんな感じなのですが、これを、イメージしてもらい、見る人に、インパクトと高感度を与えてくれて、口コミや、実際に応募がきたら嬉しいです。

㍿森川建設
A5
片面
シンプル 複雑
単色 カラフル
暗い 明るい
日常 高級
遊び心 厳粛
未来的 伝統的
女性的 男性的
一応会社のイメージカラーは、紺ですが、色は、オススメの色でお願いしたいです!
• 高解像度JPG (.jpg)
• イラストレーター形式 (.ai)
・バス広告のロゴで、バイアスを構築していますので、バス広告のデザインを利用して作っていただけると相乗効果を生むことができるので、お願いしたいです!

あ、このロゴなんか見たことあるのような感じです!
※ですが、上のロゴを入れるのが、あまり良くないと思えば、それは、気にしなくても良いです!1番は、若者を入れたいので、そのためを重視してもらいたいです!

・納品ですが、金額や、条件を少し編集できるようにしたいので、アウトライン化してるものと、されてないものを納品して頂きたいです!
A4でもA6でも使えるようにしたいです!
社内で話し合ったところ、もう少しインパクトの強い印象に残るものができるんじゃ無いかという期待を込めて延長させてもらいました。

・筋肉(鍛えられる)、
・短時間制のアルバイトがある(短時間制の職人系のアルバイトでは、珍しいです。)
・ロングタイムも、選べる。

これが1番伝えたい内容です。

次に、
職人さんは、いまとても減ってきてるので、希少性がかなり高くなっています。先に技術を学んでおくことで、後にブルーオーシャンになるのでは無いか?と予測しています。

これは、僕の伝えたい思い出もありますが、
チラシとして何を目的にしてるかは、
人を入れたいという事が目的なので、

ユーザー側の気持ちになってもらい、

・身体に自信がある人や
・身体にコンプレックスを持っていてムキムキになりたいと考えてる人
・頭を使うよりも身体を動かす事が自分に向いていると感じてる人に

響くような、チラシになることを願っています。

1発で目に引かれて、頭から離れないような、チラシにしてもらいたいです!

よろしくお願いします。

インパクトもあり、なんとなく清潔にも感じて、無駄な主張もなくシンプルで良い作品だと感じました。

多くの素晴らしい作品があり、選定するのにとても困りました。

本当にありがとうございます。

職人の価値向上を目指して、頑張ります!

本当にありがとうございました。

これからも宜しくお願い致します。

```html
<!DOCTYPE html>
<html lang="ja">
<head>
<meta charset="UTF-8">
<title>森川建設 アルバイト募集</title>
<link href="https://fonts.googleapis.com/css2?family=Noto+Sans+JP:wght@500;700;900&display=swap" rel="stylesheet">
<style>
  :root{
    --navy:#0d2a6e;
    --blue:#1e4fb0;
    --blue-light:#2f6fd6;
    --sky:#dfe6ee;
    --white:#ffffff;
    --yellow:#ffe94a;
    --ink:#123a8f;
  }
  *{margin:0;padding:0;box-sizing:border-box}
  html,body{width:847px;height:1200px;overflow:hidden;background:#fff}
  .flyer{
    position:relative;width:847px;height:1200px;overflow:hidden;
    font-family:"Noto Sans JP",sans-serif;
    background:linear-gradient(180deg,var(--blue-light) 0%,var(--blue) 45%,var(--navy) 100%);
  }
  .photo{position:absolute}
  .photo--site{left:0;top:0;width:847px;height:520px;
    background:linear-gradient(180deg,#eef2f6 0%,#c9d2dc 60%,#aeb9c6 100%);
    clip-path:polygon(0 0,100% 0,100% 62%,0 100%)}
  .photo--worker{left:438px;top:110px;width:409px;height:400px;
    background:linear-gradient(160deg,#e4e9ee 0%,#b8c2cc 55%,#8f9aa6 100%);
    clip-path:polygon(12% 0,100% 0,100% 85%,0 100%)}
  .photo--scaffold{left:0;top:420px;width:360px;height:340px;
    background:linear-gradient(180deg,#c7d8ec 0%,#97aabf 55%,#5f7088 100%);
    clip-path:polygon(0 18%,100% 0,100% 100%,0 100%)}
  .photo--team{left:24px;top:745px;width:345px;height:335px;border-radius:18px;
    background:radial-gradient(circle at 50% 35%,#f0d89a 0%,#a57a4a 45%,#2b2a3a 100%)}
  .lead{position:absolute;left:0;right:0;top:26px;text-align:center;color:var(--ink);
    font-weight:900;font-size:27px;line-height:1.55;letter-spacing:.02em}
  .headline{position:absolute;left:48px;top:128px;color:var(--white);font-weight:900;
    font-size:104px;line-height:1.02;letter-spacing:.02em;
    -webkit-text-stroke:10px var(--navy);paint-order:stroke fill}
  .pay{position:absolute;left:395px;color:var(--white);font-weight:700}
  .pay__type{font-size:30px;line-height:1.3}
  .pay__hours{font-size:27px;line-height:1.3}
  .pay__amount{display:inline-block;margin-top:6px;font-size:34px;font-weight:900;
    background:linear-gradient(transparent 62%,var(--yellow) 62%,var(--yellow) 88%,transparent 88%)}
  .pay__amount strong{font-size:60px;letter-spacing:.01em}
  .pay--long{top:520px}
  .pay--short{top:700px}
  .perks{position:absolute;left:392px;top:895px;width:430px;display:flex;flex-wrap:wrap;gap:10px}
  .perk{background:var(--white);color:var(--ink);font-weight:900;font-size:20px;
    padding:7px 14px;border-radius:4px;white-space:nowrap}
  .footer{position:absolute;left:0;right:0;bottom:0;height:112px;display:flex;
    align-items:center;justify-content:space-between;padding:0 28px}
  .contact{color:var(--white)}
  .contact__url{font-size:19px;font-weight:700;margin-bottom:10px}
  .search{display:flex;align-items:center;height:34px}
  .search__field{background:var(--white);color:#333;font-size:15px;font-weight:500;
    height:100%;padding:0 12px;display:flex;align-items:center;width:230px}
  .search__btn{background:#e8edf3;color:#333;font-size:15px;font-weight:700;height:100%;
    padding:0 12px;display:flex;align-items:center;gap:6px}
  .brand{display:flex;align-items:center;gap:14px;color:var(--white)}
  .brand__mark{width:54px;height:54px;border-radius:50%;background:var(--white)}
  .brand__name{font-size:40px;font-weight:900;letter-spacing:.06em}
</style>
</head>
<body>
<div class="flyer">
  <div class="photo photo--site" role="img" aria-label="建設現場の足場の写真"></div>
  <div class="photo photo--worker" role="img" aria-label="足場の上で作業する職人の写真"></div>
  <div class="photo photo--scaffold" role="img" aria-label="建物を囲む足場の写真"></div>
  <div class="photo photo--team" role="img" aria-label="スタッフが集まったイベントの写真"></div>

  <p class="lead">筋肉と体幹を鍛えて、ワンチャン技術も身につける！<br>筋トレ好き・格闘家・アスリートに最適！</p>

  <h1 class="headline">アルバイト<br>募集！</h1>

  <div class="pay pay--long">
    <p class="pay__type">ロングタイム</p>
    <p class="pay__hours">(8:00〜17:00)</p>
    <p class="pay__amount">日給 <strong>16,000</strong>円</p>
  </div>
  <div class="pay pay--short">
    <p class="pay__type">ショートタイム</p>
    <p class="pay__hours">(10:00〜16:00)</p>
    <p class="pay__amount">日給 <strong>13,000</strong>円</p>
  </div>

  <ul class="perks">
    <li class="perk">週休２日制</li>
    <li class="perk">イベント多数</li>
    <li class="perk">自分の用事に合わせて好きな日に休める</li>
    <li class="perk">置き場などでの残業はありません！</li>
  </ul>

  <footer class="footer">
    <div class="contact">
      <p class="contact__url">https://morikawakensetsu.info/</p>
      <div class="search">
        <span class="search__field">森川建設　社員満足度</span>
        <span class="search__btn">
          <svg width="16" height="16" viewBox="0 0 16 16" aria-hidden="true"><circle cx="6.5" cy="6.5" r="4.5" fill="none" stroke="#333" stroke-width="2"/><line x1="10" y1="10" x2="14.5" y2="14.5" stroke="#333" stroke-width="2"/></svg>
          検索
        </span>
      </div>
    </div>
    <div class="brand">
      <span class="brand__mark"></span>
      <span class="brand__name">株式会社 森川建設</span>
    </div>
  </footer>
</div>
</body>
</html>
```